Northfield Builders Guild Business card

We are looking for a new business card design with photo included.
Our business is a nonprofit construction contractor membership organization. We offer business education, assist with business setup and licensing, provide safety training, and provide a member directory.
URL: www.brickwayguildnetwork.org
Color code:
CMYK: 0 cyan, 42 magenta, 100 yellow, 0 black for Print.
Hexidecimal: #FF9900
RGB: R 255; G 153; B 0

```html
<!DOCTYPE html>
<html lang="en">
<head>
<meta charset="utf-8">
<title>Northfield Builders Guild – Business Card</title>
<link rel="stylesheet" href="https://fonts.googleapis.com/css2?family=Poppins:wght@400;500;600&display=swap">
<style>
  :root {
    --stage: #2a2a2b;
    --charcoal: #333334;
    --paper: #f4f4f4;
    --orange: #ff9900;
    --ink: #2b2b2b;
    --white: #ffffff;
    --photo-top: #c9c2bb;
    --photo-bottom: #5a4438;
  }
  * { box-sizing: border-box; margin: 0; padding: 0; }
  html, body {
    width: 1200px; height: 900px; overflow: hidden;
    background: var(--stage);
    font-family: "Poppins", sans-serif;
  }
  .stage {
    position: relative; width: 1200px; height: 900px;
  }
  .card {
    position: absolute; left: 320px; width: 560px; height: 320px;
    overflow: hidden; border-radius: 3px;
    box-shadow: 0 18px 40px rgba(0,0,0,0.45);
    border-bottom: 3px solid var(--orange);
  }
  .card--front { top: 95px; background: var(--paper); }
  .card--back { top: 470px; background: var(--charcoal); }

  .front-band { position: absolute; inset: 0; width: 560px; height: 320px; }

  .holder { position: absolute; left: 48px; top: 42px; }
  .holder__name { color: var(--orange); font-size: 24px; font-weight: 600; line-height: 1.2; }
  .holder__role { color: var(--white); font-size: 14px; font-weight: 400; margin-top: 2px; }

  .portrait {
    position: absolute; left: 402px; top: 28px;
    width: 130px; height: 130px; border-radius: 50%;
    border: 3px solid var(--orange);
    background: radial-gradient(circle at 50% 40%, var(--photo-top) 0%, #a08878 45%, var(--photo-bottom) 100%);
  }

  .contact { position: absolute; left: 48px; top: 168px; list-style: none; }
  .contact__item {
    display: flex; align-items: center; gap: 10px;
    color: var(--ink); font-size: 13.5px; line-height: 22px;
  }
  .contact__icon { width: 14px; height: 14px; flex: none; }

  .address {
    position: absolute; left: 48px; top: 248px;
    color: var(--ink); font-size: 13.5px; line-height: 20px; font-style: normal;
  }

  .wordmark {
    position: absolute; right: 34px; top: 196px; width: 170px; text-align: right;
    color: var(--ink); font-size: 19px; font-weight: 600; line-height: 1.15;
  }

  .wordmark--back {
    position: absolute; left: 0; right: 0; top: 50%; transform: translateY(-50%);
    text-align: center; color: var(--orange);
    font-size: 40px; font-weight: 600; line-height: 1.15;
  }
</style>
</head>
<body>
<main class="stage">

  <section class="card card--front">
    <svg class="front-band" viewBox="0 0 560 320" aria-hidden="true">
      <polygon points="0,0 560,0 560,80 0,132" fill="var(--charcoal)"/>
      <line x1="0" y1="133" x2="560" y2="81" stroke="var(--orange)" stroke-width="3"/>
    </svg>

    <div class="holder">
      <p class="holder__name">Morgan Ellery</p>
      <p class="holder__role">Director</p>
    </div>

    <div class="portrait" role="img" aria-label="Portrait photo of the director"></div>

    <ul class="contact">
      <li class="contact__item">
        <svg class="contact__icon" viewBox="0 0 24 24" aria-hidden="true"><path d="M5 3h4l2 5-3 2a12 12 0 0 0 6 6l2-3 5 2v4a2 2 0 0 1-2 2A18 18 0 0 1 3 5a2 2 0 0 1 2-2z" fill="none" stroke="var(--orange)" stroke-width="2" stroke-linejoin="round"/></svg>
        (503) 555-0148
      </li>
      <li class="contact__item">
        <svg class="contact__icon" viewBox="0 0 24 24" aria-hidden="true"><rect x="3" y="5" width="18" height="14" rx="2" fill="none" stroke="var(--orange)" stroke-width="2"/><path d="M3 7l9 6 9-6" fill="none" stroke="var(--orange)" stroke-width="2"/></svg>
        info@brickwayguildnetwork.org
      </li>
      <li class="contact__item">
        <svg class="contact__icon" viewBox="0 0 24 24" aria-hidden="true"><circle cx="12" cy="12" r="9" fill="none" stroke="var(--orange)" stroke-width="2"/><path d="M3 12h18M12 3c3 3 3 15 0 18M12 3c-3 3-3 15 0 18" fill="none" stroke="var(--orange)" stroke-width="2"/></svg>
        brickwayguildnetwork.org
      </li>
    </ul>

    <address class="address">
      2450 Cedar Ridge Avenue<br>
      Millbrook, OR 97000
    </address>

    <p class="wordmark">Northfield Builders Guild</p>
  </section>

  <section class="card card--back">
    <p class="wordmark--back">Northfield<br>Builders Guild</p>
  </section>

</main>
</body>
</html>
```